Business Card Design Project

Hello,

We have just created our new COMPANY LOGO via Pixel Harbor and would not like to turn our attention to new Business Cards.

We are a printing company based in Singapore & Las Vegas. We specialize in blue-print printing for the Architectural, Engineering and Construction industries

The design should be simple, professional, clean and organized.

The Business Cards should "pop" when seen and will hopefully be something that makes you look twice.

We have two different Pan-tones that we use for our company, feel free to use them if you think they will work for your design?

Orange: PMS 021
Gray: PMS 431

I have attached our current logo for your use and reference which should obvious be on our business cards.

Considering we have two locations on different continents, we need business cards templates where the address details need to be interchangeable for each different location (total 2)

First one:
38 Merrow Lane #03-11 to #03-15
Singapore 528473
Tel : +65 6847-3920
Fax : +65 6843-7702

Second one:
2381 W. Tanfield Rd, Suite 204
Las Vegas, Nevada 89152
Tel : (702) 555-4137
Fax : (702) 555-4189

We would also like to list a few of our key services on the card. Here are a few examples to get you going.

Plan Printing & Plotting
Digital Colour Printing
Cadline Printing
Specialty Book Making
Scanning & Archiving
Collection & Delivey

This is the first time i have requested for business cards to be created so please let me know if you require any additional information.
Many Thanks,
Tobin
Updates

Project Deadline Extended
Reason: It took us longer than expected to finalize our Company Logo We look forward to receiving your designs.

Target Market(s)

Our Target Market is construction related people.
Construction
Architecture
Engineering

Industry/Entity Type

Printing

Font styles to use
Other font styles liked:
• Times New Roman

Colors
faa54b
ffffff

Requirements
Must have
• The business card must have our Company Logo (attached)
The font used must be Times New Roman
Should not have
• Playful images of print designs and/or logos

```html
<!DOCTYPE html>
<html lang="en">
<head>
<meta charset="utf-8">
<title>Tandem Plan Works – Business Card</title>
<link href="https://fonts.googleapis.com/css2?family=Tinos:wght@400;700&display=swap" rel="stylesheet">
<style>
  :root{
    --orange:#e8642a;
    --orange-light:#f58a4a;
    --orange-deep:#d4521d;
    --gold:#f6b23c;
    --white:#ffffff;
    --paper:#f4f4f2;
    --stage:#e9e6e1;
  }
  *{margin:0;padding:0;box-sizing:border-box}
  html,body{width:1200px;height:1023px;overflow:hidden}
  body{background:var(--stage);font-family:"Tinos","Times New Roman",serif;position:relative}
  .card{position:absolute;width:525px;height:300px;overflow:hidden;box-shadow:0 6px 18px rgba(0,0,0,.18)}
  .card-front{left:90px;top:110px;background:var(--paper)}
  .card-back{left:585px;top:600px;background:linear-gradient(120deg,var(--orange-deep),var(--orange) 55%,var(--orange-light))}
  .card svg.bands{position:absolute;inset:0}

  .top-row{position:absolute;left:0;right:0;top:14px;display:flex;justify-content:space-between;padding:0 22px;color:var(--white);font-size:13px}
  .holder{text-align:center;margin-top:-4px}
  .holder .name{font-weight:700;font-size:17px;letter-spacing:1px}
  .holder .role{font-size:12px}

  .identity{position:absolute;left:0;right:0;top:108px;text-align:center;color:var(--orange-light)}
  .identity .mark{font-size:44px;line-height:1;margin-bottom:6px}
  .identity .company{font-weight:700;font-size:20px}
  .identity .tagline{font-size:14px}

  .address{position:absolute;right:26px;bottom:14px;text-align:center;color:var(--white);font-size:13.5px;line-height:1.35}

  .back-mark{position:absolute;left:120px;top:20px;font-size:200px;color:rgba(150,50,10,.18);line-height:1}
  .back-identity{position:absolute;right:26px;top:28px;text-align:right;color:var(--white)}
  .back-identity .company{font-weight:700;font-size:20px}
  .back-identity .tagline{font-weight:700;font-style:italic;font-size:13px}
  .services{position:absolute;left:20px;right:20px;bottom:26px;display:flex;color:var(--white);font-size:12.5px;line-height:1.5}
  .services li{list-style:none;flex:1;padding:0 12px}
  .services li + li{border-left:1px solid rgba(255,255,255,.75)}
</style>
</head>
<body>

<section class="card card-front">
  <svg class="bands" viewBox="0 0 525 300" aria-hidden="true">
    <path d="M0 0H525V58Q290 55 0 90Z" fill="var(--orange)"/>
    <path d="M0 90Q290 55 525 58" fill="none" stroke="var(--gold)" stroke-width="3"/>
    <path d="M0 268Q260 255 525 208V300H0Z" fill="var(--orange)"/>
    <path d="M0 268Q260 255 525 208" fill="none" stroke="var(--gold)" stroke-width="3"/>
  </svg>
  <div class="top-row">
    <span class="tel">[T] (702) 555-4137</span>
    <div class="holder"><div class="name">MARCUS HALE</div><div class="role">Director</div></div>
    <span class="fax">(702) 555-4189 [F]</span>
  </div>
  <div class="identity">
    <div class="mark">TPW</div>
    <div class="company">Tandem Plan Works</div>
    <div class="tagline">A Member of the TPW Group of Companies</div>
  </div>
  <div class="address">2381 W. Tanfield Rd, Suite 204<br>Las Vegas, Nevada 89152</div>
</section>

<section class="card card-back">
  <div class="back-mark">TPW</div>
  <div class="back-identity">
    <div class="company">Tandem Plan Works</div>
    <div class="tagline">A Member of the TPW Group of Companies</div>
  </div>
  <ul class="services">
    <li>Printing &amp; Plotting<br>Colour Printing</li>
    <li>Cadline Printing<br>Specialty Book Making</li>
    <li>Scanning &amp; Archiving<br>Collection &amp; Delivey</li>
  </ul>
</section>

</body>
</html>
```